Honey Bottle Labels for Honey Business

The honey is a niche product and the logo should exude a strong impression of wild and raw honey and natural – as in natural beekeeping. We try to keep things as simple as possible; this includes the processes the honey goes through.
We are looking for something with a gourmet / classy upmarket look and feel design. For example: Ideas with bees, honeycomb, modern or hexagonal feature; something eye catching, but not too busy.
Our honey is all natural and organic. We are a clean, simple yet sophisticated business, so would like our logo to reflect these principles.

Feel free to expand your creativity to anything you may think would look awesome and original!

The label needs to contain:
1. Our company logo. (Please see attached)
2. 100% Pure Raw Honey / Local
3. Net Wt: 16 oz (454 g) (this is the weight of the honey and will need to be modified based on bottle size.)
4. Address, Cedar Hollow, MN 56100 (not larger than 1/16th inch)

Needs to be versatile to include possibility of clear label, I have included some example pictures as ideas (oval, round, square tags)

Sizes needed:
Large oval 2 5/8" x 4 1/2"
Small oval: 1 3/4" wide x 3" tall
Rectangle 1 3/4" tall x 5" wide
Round diameter 2.5"

Target Market(s)

Gourmet stores, market stall, local tourist market, potential store door sales

Requirements
Must have
• - A design that can be used on various packaging, jars and containers. We are hoping to scale up the production and want something to suit.
• - has to have a wow to stand out on the supermarket shelves
Nice to have
• Things we like:
• Minimalist designs
• Clever designs
• We don't like hand drawn font types
• We are open to the use of a hexagon in the logo, but not must have
Should not have
• Things we do not like:
• Too many colors

```html
<!DOCTYPE html>
<html lang="en">
<head>
<meta charset="utf-8">
<title>Amberfield Honey – Rectangle Jar Label</title>
<link href="https://fonts.googleapis.com/css2?family=Arimo:wght@400&family=Ubuntu+Condensed&display=swap" rel="stylesheet">
<style>
  :root {
    --canvas: #e9e9e9;
    --label-edge: #9a9a9a;
    --frame-black: #0d0d0d;
    --paper: #ffffff;
    --honey-light: #fbd77a;
    --honey: #f5b82e;
    --honey-deep: #e9a51a;
    --ink: #1a1a1a;
  }
  * { margin: 0; padding: 0; box-sizing: border-box; }
  html, body {
    width: 1200px;
    height: 1200px;
    overflow: hidden;
    background: var(--canvas);
  }
  .stage {
    position: relative;
    width: 1200px;
    height: 1200px;
  }
  .label {
    position: absolute;
    left: 150px;
    top: 442px;
    width: 900px;
    height: 315px;
    background: var(--frame-black);
    border: 3px solid var(--label-edge);
    box-shadow: 0 4px 10px rgba(0,0,0,0.25);
  }
  .label__comb {
    position: absolute;
    inset: 14px;
    background: var(--paper);
  }
  .label__comb svg { display: block; width: 100%; height: 100%; }
  .label__claim {
    position: absolute;
    left: 60px;
    top: 138px;
    font-family: "Ubuntu Condensed", sans-serif;
    font-size: 23px;
    line-height: 1;
    color: var(--ink);
    letter-spacing: -0.3px;
    white-space: nowrap;
  }
  .brand {
    position: absolute;
    left: 347px;
    top: 42px;
    width: 200px;
    height: 220px;
    display: flex;
    flex-direction: column;
    align-items: center;
    justify-content: center;
    gap: 14px;
  }
  .brand__dot {
    width: 46px;
    height: 46px;
    border-radius: 50%;
    background: var(--honey);
  }
  .brand__name {
    font-family: "Arimo", sans-serif;
    font-size: 28px;
    line-height: 1.15;
    color: var(--honey-deep);
    text-align: center;
  }
  .label__weight {
    position: absolute;
    left: 626px;
    top: 104px;
    font-family: "Arimo", sans-serif;
    font-size: 21px;
    line-height: 1;
    color: var(--ink);
    white-space: nowrap;
  }
  .label__address {
    position: absolute;
    left: 640px;
    top: 182px;
    display: flex;
    align-items: center;
    gap: 6px;
    font-family: "Arimo", sans-serif;
    font-size: 13px;
    line-height: 1;
    color: var(--ink);
    white-space: nowrap;
  }
  .label__address svg { width: 12px; height: 16px; }
</style>
</head>
<body>
<main class="stage">
  <section class="label">
    <div class="label__comb">
      <svg viewBox="0 0 866 281" preserveAspectRatio="none" role="img" aria-label="Honeycomb pattern border with small bee emblems framing the label">
        <defs>
          <linearGradient id="combTone" x1="0" y1="0" x2="1" y2="1">
            <stop offset="0" stop-color="#f5b82e"/>
            <stop offset="0.5" stop-color="#fbd77a"/>
            <stop offset="1" stop-color="#f5b82e"/>
          </linearGradient>
        </defs>
        <path fill="url(#combTone)" fill-rule="evenodd"
          d="M0 0H866V281H0Z
             M24 34 Q60 30 110 50 Q200 28 300 40 Q380 34 420 20 Q500 30 560 46 Q640 24 740 36 Q800 30 842 48
             L846 230 Q800 250 740 238 Q660 250 600 232 Q520 250 440 232 Q360 250 280 230 Q200 250 120 232 Q70 244 24 236Z"/>
      </svg>
    </div>

    <p class="label__claim">100% Pure Raw Honey</p>

    <div class="brand">
      <span class="brand__dot"></span>
      <span class="brand__name">Amberfield<br>Honey</span>
    </div>

    <p class="label__weight">Net Wt: 16 oz (454 g)</p>

    <p class="label__address">
      <svg viewBox="0 0 12 16" aria-hidden="true">
        <path d="M6 1a4.5 4.5 0 0 0-4.5 4.5C1.5 9 6 15 6 15s4.5-6 4.5-9.5A4.5 4.5 0 0 0 6 1z" fill="#f5b82e" stroke="#1a1a1a" stroke-width="1"/>
        <circle cx="6" cy="5.5" r="1.6" fill="#ffffff"/>
      </svg>
      Cedar Hollow, MN 56100
    </p>
  </section>
</main>
</body>
</html>
```